4Star Hotel looking for web design

Hello everyone,
We are located in Cambodia, the hotel should open in 2-3 months. The name will be Velmora-Boutique Hotel. We are looking for a webdesign which is professional, elegant and SIMPLE.
All informations should be easy to find. We are quite open to proposition but we would like to the home page:
-a carousel with around 5-8 picture
-Little menu where we can book a room
By the way, we would like a page for our restaurant, gallery, contact page for description of the rooms. I add some old pictures.
I give an example of what we are expecting:
www.brenquastays.com/torvelhill
We hope that we are proposing a good job for you guys. Have fun and Thanks.
Oh and the winner ( or someone he had choose) of course have free night in our presidential suite
Target Market(s)
We are looking for european Market. Let s say people middle age who are willing to travel in difficult area
Industry/Entity Type
Hotel
Coding
Coded - Design and coding required
Number of Pages Required
5+ page
Requirements
Must have
- Simple, simple and Simple
- Carousel
- place for book a room
- during booking, a menu for select room , and after that another menu for propose like tour in town, taxi, flower, bottle of champagne for example
- during all the process, the customer should be able to know at what step it is and can stop and come back after
- Have to be perfect for smartphone
- Price with drawbar for they know how much they earn with our reduction
Nice to have
- during the process of information (name, adress, tel...), it would be great if they can fill it with a button facebook, google plus, lindkdin, instagram ....
- then a button share on facebook, twitter for know that they book in our hotel
- At the end of the booking, a flashcode with the recapitulatif that customer can scan.

```html
<!DOCTYPE html>
<html lang="en">
<head>
<meta charset="utf-8">
<title>Velmora-Boutique Hotel</title>
<link href="https://fonts.googleapis.com/css2?family=Lato:wght@400;700;900&display=swap" rel="stylesheet">
<style>
:root{
  --red:#a8321a;
  --red-deep:#5b0f07;
  --red-dark:#3c0703;
  --ink:#2a2a2a;
  --muted:#8a8a8a;
  --line:#dddddd;
  --panel:#f1f1f1;
  --white:#ffffff;
}
*{box-sizing:border-box;margin:0;padding:0}
html,body{width:1200px;height:2440px;overflow:hidden}
body{font-family:'Lato',sans-serif;color:var(--ink);background:var(--white);position:relative}

/* header */
.site-header{position:absolute;top:0;left:0;width:1200px;height:64px;background:var(--white);border-bottom:1px solid var(--line)}
.brand{position:absolute;left:60px;top:14px;display:flex;align-items:center;gap:10px}
.brand-mark{width:34px;height:34px;background:var(--red-deep)}
.brand-name{font-size:15px;font-weight:700;color:var(--red-deep);line-height:1.1;width:90px}
.utility{position:absolute;right:60px;top:6px;display:flex;gap:22px;font-size:10px;color:#555}
.utility span::before{content:"";display:inline-block;width:7px;height:7px;border-radius:50%;background:var(--red);margin-right:5px}
.main-nav{position:absolute;right:60px;top:34px;display:flex;gap:26px;font-size:14px}
.main-nav a{color:#444;text-decoration:none}
.main-nav a.active{color:var(--red);font-weight:700}
.dropdown{position:absolute;left:492px;top:64px;width:160px;background:var(--red);padding:6px 0;z-index:3}
.dropdown li{list-style:none;font-size:11px;color:var(--white);padding:5px 16px;border-bottom:1px solid rgba(255,255,255,.15)}
.dropdown li.current{background:var(--white);color:var(--red)}

/* hero */
.hero{position:absolute;top:64px;left:0;width:1200px;height:484px}
.hero-photo{position:absolute;inset:0;background:linear-gradient(180deg,#bfbfbf 0%,#9a9a9a 35%,#6c6c6c 60%,#3b3b3b 100%)}
.hero-arrow{position:absolute;top:210px;width:40px;height:40px;background:rgba(0,0,0,.55)}
.hero-arrow.prev{left:0}.hero-arrow.next{right:0}
.hero-caption{position:absolute;left:0;bottom:0;width:1200px;height:76px;background:rgba(0,0,0,.55)}
.hero-caption h1{position:absolute;left:60px;top:14px;color:var(--white);font-size:22px;font-weight:900;letter-spacing:.5px}
.hero-caption p{position:absolute;left:60px;top:44px;color:#ddd;font-size:12px}
.book-now{position:absolute;right:60px;top:18px;color:var(--white);text-align:center;font-weight:900;font-size:15px}
.book-now small{display:block;font-size:9px;font-weight:400;color:#ccc}

/* availability */
.availability-band{position:absolute;top:548px;left:0;width:1200px;height:100px;background:var(--red-deep);display:flex;align-items:center;justify-content:center}
.availability-band h2{color:var(--white);font-size:34px;font-weight:900;letter-spacing:1px}
.booking-form{position:absolute;top:648px;left:0;width:1200px;height:172px;background:var(--panel);border-bottom:1px solid var(--line)}
.field{position:absolute;top:50px}
.field label{display:block;font-size:12px;color:#555;margin-bottom:8px}
.field .input{height:34px;background:var(--white);border:1px solid #ccc;font-size:11px;color:#555;padding:10px 8px;position:relative}
.field .input.select::after{content:"";position:absolute;right:10px;top:14px;border:4px solid transparent;border-top-color:#666}
.check-btn{position:absolute;left:966px;top:75px;width:172px;height:34px;background:var(--red);color:var(--white);font-size:12px;font-weight:700;display:flex;align-items:center;justify-content:center}

/* features */
.welcome{position:absolute;top:880px;left:0;width:1200px;text-align:center}
.welcome h2{font-size:38px;font-weight:900;color:var(--ink)}
.welcome h2 span{color:var(--red)}
.welcome p{margin:22px auto 0;width:560px;font-size:13px;color:var(--muted);line-height:1.6}
.features{position:absolute;top:1070px;left:60px;width:1080px;display:flex;justify-content:space-between}
.feature{width:300px;text-align:center}
.feature-icon{width:140px;height:140px;border-radius:50%;background:var(--red);margin:0 auto;display:flex;align-items:center;justify-content:center}
.feature-icon.dark{background:var(--red-dark)}
.feature h3{margin-top:26px;font-size:15px;font-weight:700;text-transform:uppercase}
.feature p{margin-top:12px;font-size:12px;color:var(--muted);line-height:1.6}
.read-more{display:inline-block;margin-top:34px;width:150px;height:40px;line-height:40px;background:var(--red);color:var(--white);font-size:13px}
.read-more.dark{background:var(--red-dark)}

/* latest */
.latest{position:absolute;top:1560px;left:0;width:1200px;height:700px;border-top:1px solid var(--line)}
.latest::after{content:"";position:absolute;left:760px;top:40px;width:1px;height:620px;background:var(--line)}
.section-title{font-size:24px;font-weight:900;color:var(--ink);padding-bottom:12px;border-bottom:3px solid var(--red);display:inline-block}
.section-title span{color:var(--red)}
.reviews{position:absolute;left:60px;top:40px;width:620px}
.review{margin-top:34px}
.review-top{display:flex;gap:20px}
.review-photo{width:240px;height:150px;background:linear-gradient(135deg,#6a3a22,#2e1a10 60%,#8c5a32)}
.review h4{font-size:17px;font-weight:900;color:var(--red-dark);line-height:1.2;width:150px}
.review .date{font-size:12px;color:#555;margin-top:12px}
.dots{display:flex;gap:6px;margin-top:14px}
.dots i{width:10px;height:10px;border-radius:50%;background:#ccc}
.dots i.on{background:var(--ink)}
.review p{margin-top:14px;font-size:11px;color:var(--muted);line-height:1.7}
.news{position:absolute;left:800px;top:40px;width:340px}
.news-item{display:flex;gap:18px;margin-top:40px}
.news-date{width:44px;text-align:center;flex:none}
.news-date b{display:block;background:var(--red);color:var(--white);font-size:17px;height:36px;line-height:36px}
.news-date span{font-size:11px;color:#555}
.news-item h5{font-size:15px;color:var(--red);font-weight:400}
.news-item p{font-size:11px;color:var(--muted);line-height:1.6;margin-top:4px}

/* footer */
.site-footer{position:absolute;top:2260px;left:0;width:1200px;height:180px;background:var(--red-deep)}
.footer-nav{display:flex;justify-content:center;gap:26px;margin-top:34px;font-size:12px;color:var(--white);text-transform:uppercase}
.social{display:flex;justify-content:center;gap:14px;margin-top:20px}
.social i{width:32px;height:32px;background:#2f6db5;border-radius:3px}
.copyright{position:absolute;bottom:0;left:0;width:1200px;height:38px;background:var(--red-dark);color:#d9b9b3;font-size:11px;text-align:center;line-height:38px}
</style>
</head>
<body>

<header class="site-header">
  <div class="brand"><div class="brand-mark"></div><div class="brand-name">Velmora Boutique</div></div>
  <div class="utility"><span>Languages</span><span>Create Account</span><span>Log In</span></div>
  <nav class="main-nav">
    <a href="#">Home</a><a href="#" class="active">Accommodation</a><a href="#">Restaurant &amp; Bar</a><a href="#">Meeting and events</a><a href="#">Blog</a><a href="#">Special packages</a>
  </nav>
</header>
<ul class="dropdown">
  <li>Suite</li><li class="current">Junior Suite</li><li>Family room</li><li>Cambodia Room</li><li>Deluxe room</li><li>Standard room</li>
</ul>

<section class="hero">
  <div class="hero-photo" role="img" aria-label="Black and white view over the river and treetops near the hotel"></div>
  <div class="hero-arrow prev"><svg width="40" height="40"><path d="M24 12 L16 20 L24 28" stroke="#fff" stroke-width="3" fill="none"/></svg></div>
  <div class="hero-arrow next"><svg width="40" height="40"><path d="M16 12 L24 20 L16 28" stroke="#fff" stroke-width="3" fill="none"/></svg></div>
  <div class="hero-caption">
    <h1>WELCOME TO VELMORA</h1>
    <p>Lorem Ipsum is simply dummy text of the printing and typesetting</p>
    <div class="book-now">BOOK NOW<small>BEST RATES AVAILABLE</small></div>
  </div>
</section>

<div class="availability-band"><h2>CHECK AVAILABILITY</h2></div>
<section class="booking-form">
  <div class="field" style="left:60px;width:190px"><label>Check in</label><div class="input">06-07-2013</div></div>
  <div class="field" style="left:270px;width:130px"><label>Night</label><div class="input select">1</div></div>
  <div class="field" style="left:420px;width:190px"><label>Check out</label><div class="input">06-07-2013</div></div>
  <div class="field" style="left:630px;width:130px"><label>Adults</label><div class="input select">1</div></div>
  <div class="field" style="left:780px;width:150px"><label>Children</label><div class="input select">0</div></div>
  <div class="check-btn">CHECK AVAILABILITY</div>
</section>

<section class="welcome">
  <h2><span>WE LOVE</span> VELMORA HOTEL</h2>
  <p>Lorem Ipsum is simply dummy text of the printing and typesetting industry. Lorem Ipsum has been the</p>
</section>

<section class="features">
  <div class="feature">
    <div class="feature-icon"><svg width="64" height="64" viewBox="0 0 64 64" fill="none" stroke="#fff" stroke-width="4"><path d="M18 44 L16 20 L32 30 L48 20 L46 44 Z"/><path d="M18 52 H46"/></svg></div>
    <h3>Luxury accommodations</h3>
    <p>Praesent vestibulum mole lacus. Aenean nonummy hendrerit mauris. Phasellus suscipit varius mi. Cum sociis natoque penatibus et magnis dis parturient montes.</p>
    <a class="read-more">Read More</a>
  </div>
  <div class="feature">
    <div class="feature-icon dark"><svg width="64" height="64" viewBox="0 0 64 64" fill="none" stroke="#fff" stroke-width="4"><rect x="10" y="14" width="44" height="30"/><path d="M24 52 H40 M32 44 V52"/></svg></div>
    <h3>Online reservation</h3>
    <p>Praesent vestibulum mole lacus. Aenean nonummy hendrerit mauris. Phasellus suscipit varius mi. Cum sociis natoque penatibus et magnis dis parturient montes.</p>
    <a class="read-more dark">Read More</a>
  </div>
  <div class="feature">
    <div class="feature-icon"><svg width="64" height="64" viewBox="0 0 64 64" fill="none" stroke="#fff" stroke-width="4"><rect x="14" y="26" width="36" height="26"/><path d="M10 26 H54 M32 26 V52 M32 26 C24 12 16 20 32 26 C48 20 40 12 32 26"/></svg></div>
    <h3>Special offer</h3>
    <p>Praesent vestibulum mole lacus. Aenean nonummy hendrerit mauris. Phasellus suscipit varius mi. Cum sociis natoque penatibus et magnis dis parturient montes.</p>
    <a class="read-more">Read More</a>
  </div>
</section>

<section class="latest">
  <div class="reviews">
    <h3 class="section-title"><span>LATEST</span> REVIEWS</h3>
    <article class="review">
      <div class="review-top">
        <div class="review-photo" role="img" aria-label="Hotel lobby lit in warm evening light"></div>
        <div><h4>LOREM IPSUM IS DUMMY TEXT</h4><div class="date">06 May 2013</div><div class="dots"><i class="on"></i><i class="on"></i><i></i><i></i><i></i></div></div>
      </div>
      <p>Praesent vestibulum mole lacus. Aenean nonummy hendrerit mauris. Phasellus suscipit varius mi. Cum sociis natoque penatibus et magnis dis parturient montes, nascetur ridiculus mus. Nulla dui fusce feugiat malesuada odio morbi nunc odio gravida at cursus nec luctus.</p>
    </article>
    <article class="review">
      <div class="review-top">
        <div class="review-photo" role="img" aria-label="Hotel restaurant dining room with set tables"></div>
        <div><h4>LOREM IPSUM IS DUMMY TEXT</h4><div class="date">06 May 2013</div><div class="dots"><i class="on"></i><i class="on"></i><i></i><i></i><i></i></div></div>
      </div>
      <p>Praesent vestibulum mole lacus. Aenean nonummy hendrerit mauris. Phasellus suscipit varius mi. Cum sociis natoque penatibus et magnis dis parturient montes, nascetur ridiculus mus. Nulla dui fusce feugiat malesuada odio.</p>
    </article>
  </div>
  <div class="news">
    <h3 class="section-title"><span>LATEST</span> NEWS</h3>
    <div class="news-item"><div class="news-date"><b>28</b><span>May</span></div><div><h5>News from us from now</h5><p>Donec ullamcorper nulla non metus auctor fringilla. Donec sed odio dui.</p></div></div>
    <div class="news-item"><div class="news-date"><b>05</b><span>May</span></div><div><h5>News from us from now</h5><p>Donec ullamcorper nulla non metus auctor fringilla. Donec sed odio dui.</p></div></div>
    <div class="news-item"><div class="news-date"><b>28</b><span>May</span></div><div><h5>News from us from now</h5><p>Donec ullamcorper nulla non metus auctor fringilla. Donec sed odio dui.</p></div></div>
    <div class="news-item"><div class="news-date"><b>28</b><span>May</span></div><div><h5>News from us from now</h5><p>Donec ullamcorper nulla non metus auctor fringilla. Donec sed odio dui.</p></div></div>
  </div>
</section>

<footer class="site-footer">
  <nav class="footer-nav"><span>Home</span><span>Accommodation</span><span>Restaurant &amp; Bar</span><span>Meeting and events</span><span>Blog</span><span>Special packages</span></nav>
  <div class="social"><i></i><i></i><i style="background:#c0392b"></i><i style="background:#1f6f9f"></i></div>
  <div class="copyright">© 2013 ALL RIGHTS RESERVED</div>
</footer>

</body>
</html>
```